Surgical Procedure Room Letterhead

PLEASE DO NOT MAKE YOUR LETTERHEAD SIMILAR TO THE ONE I AM INCLUDING IN MY UPLOADS

Hello! I need my logo used to make a very clean, professional, simple letterhead that has all the pertinent information in it:
Location: 4829 NW 58th Lane, Suite 310
Tamarac, FL 33468
Phone: 954-618-2450
Fax: 800-394-8261

Can you please put this all on a word document that is easily editable? I will include my practice letterhead as an example ONLY of how easy it should be to write below the letterhead. Please don't make this letterhead the same as the one I am including in this example. They are two separate businesses.

Target Market(s)

Insurance companies

Industry/Entity Type

medical

Requirements
Must have
• classiness, elegance, simplicity
Should not have
• Please don't make your letterhead the same as the one that I included in my uploads

```html
<!DOCTYPE html>
<html lang="en">
<head>
<meta charset="utf-8">
<title>Meridian Care Suites – Letterhead</title>
<link rel="stylesheet" href="https://fonts.googleapis.com/css2?family=Open+Sans:wght@400;600;700&display=swap">
<style>
  :root {
    --navy: #0f3a66;
    --gold: #d4ad3b;
    --ink: #222428;
    --body: #55585e;
    --backdrop: #e9eaec;
    --paper: #ffffff;
    --sig-tone: #e4e4e6;
  }
  * { margin: 0; padding: 0; box-sizing: border-box; }
  html, body { width: 999px; height: 1200px; overflow: hidden; }
  body {
    background: var(--backdrop);
    font-family: "Open Sans", Arial, sans-serif;
    color: var(--ink);
    position: relative;
  }
  .letterhead {
    position: absolute;
    left: 71px; top: 0;
    width: 857px; height: 1200px;
    background: var(--paper);
  }
  .brand {
    position: absolute; left: 66px; top: 92px;
    display: flex; align-items: center; gap: 14px;
  }
  .brand-dot { width: 42px; height: 42px; border-radius: 50%; background: var(--gold); }
  .brand-name {
    font-weight: 600; font-size: 30px; color: var(--navy);
    letter-spacing: 0.5px; line-height: 1;
  }
  .header-rule { position: absolute; left: 56px; top: 216px; }
  .sender { position: absolute; left: 66px; top: 284px; }
  .sender-name { font-size: 22px; font-weight: 600; color: var(--navy); line-height: 1.2; }
  .sender-title { font-size: 12.5px; color: var(--ink); margin-top: 2px; margin-bottom: 10px; }
  .sender-line { font-size: 15px; line-height: 23.5px; color: var(--ink); }
  .sender-line b { color: var(--gold); font-weight: 700; display: inline-block; width: 30px; }
  .letter-date {
    position: absolute; right: 72px; top: 378px;
    font-size: 15px; color: var(--ink);
  }
  .letter-body { position: absolute; left: 66px; top: 458px; width: 719px; }
  .letter-body p { margin-bottom: 30px; }
  .letter-body span {
    display: block; white-space: nowrap; overflow: hidden;
    font-size: 14.5px; line-height: 32px; color: var(--body);
  }
  .signoff { position: absolute; left: 602px; top: 1000px; width: 160px; text-align: center; }
  .signature-mark { width: 150px; height: 38px; margin: -188px auto 10px; background: var(--sig-tone); border-radius: 4px; }
  .signoff { top: 1012px; }
  .signer-name { font-size: 14.5px; font-weight: 700; line-height: 1.2; }
  .signer-role { font-size: 14px; line-height: 1.2; }
  .footer-contact { position: absolute; left: 66px; top: 1030px; color: var(--body); }
  .footer-line { display: flex; align-items: center; gap: 8px; font-size: 16px; line-height: 27px; }
  .footer-address { font-size: 15px; line-height: 19px; margin-top: 8px; }
</style>
</head>
<body>
  <main class="letterhead">
    <div class="brand">
      <span class="brand-dot"></span>
      <span class="brand-name">Meridian Care Suites</span>
    </div>

    <svg class="header-rule" width="740" height="14" viewBox="0 0 740 14">
      <polygon points="4,2 230,2 226,13 0,13" fill="var(--gold)"/>
      <rect x="229" y="6" width="510" height="3" fill="var(--navy)"/>
    </svg>

    <section class="sender">
      <div class="sender-name">Ellen Marsh</div>
      <div class="sender-title">Chief Director</div>
      <div class="sender-line"><b>A :</b>12-4, Harbor Lane Singapore - 7410</div>
      <div class="sender-line"><b>W :</b>mail@meridiancare.com, www.meridiancare.com</div>
      <div class="sender-line"><b>P :</b>+880 - 24680 - 1357</div>
    </section>

    <div class="letter-date">Date, 10 September, 2019</div>

    <article class="letter-body">
      <p>
        <span>This is a sample letter that has been placed to demonstrate typing remat (Your Company). letterhead</span>
        <span>design. When positioned properly, it will serve to work in harmony with all other elements letterhead.</span>
        <span>This letterhead design is meant to project an image</span>
      </p>
      <p>
        <span>This letterhead design is meant project an image of professionalism reliability. By using simple aligen</span>
        <span>we have created a very spacious feeling. The simplicity suggest&nbsp; rengththe spaciousnes contributes h</span>
        <span>aesthetics the layout. These basic qualities along with the (Your Company)</span>
      </p>
      <p>
        <span>look and helps reinforce the (Your Company) brand. letterhead design is meant to project an image p</span>
        <span>design. When positioned properly, it will serve to work in harmony all the other elements letterhead.</span>
        <span>sionalism and reliability.</span>
      </p>
    </article>

    <div class="signoff" style="top:858px;">
      <div class="signature-mark" role="img" aria-label="Handwritten signature of the manager" style="margin:0 auto 8px;"></div>
      <div class="signer-name">Daniel Crowe</div>
      <div class="signer-role">Manager</div>
    </div>

    <footer class="footer-contact">
      <div class="footer-line">
        <svg width="15" height="15" viewBox="0 0 16 16" aria-hidden="true">
          <rect width="16" height="16" rx="3" fill="var(--navy)"/>
          <path d="M5 3.5l1.8 2.2-1 1.3c.7 1.4 1.8 2.5 3.2 3.2l1.3-1L12.5 11l-1.2 1.5C7.5 12.3 3.7 8.5 3.5 4.7z" fill="#fff"/>
        </svg>
        954-618-2450
      </div>
      <div class="footer-line">
        <svg width="15" height="15" viewBox="0 0 16 16" aria-hidden="true">
          <rect width="16" height="16" rx="3" fill="var(--navy)"/>
          <rect x="5" y="3" width="6" height="3" fill="#fff"/>
          <rect x="3" y="6.5" width="10" height="4.5" rx="1" fill="#fff"/>
          <rect x="5" y="10" width="6" height="3" fill="#fff" stroke="var(--navy)" stroke-width="0.8"/>
        </svg>
        800-394-8261
      </div>
      <div class="footer-address">4829 NW 58th Lane, Suite 310<br>Tamarac, FL 33468</div>
    </footer>
  </main>
</body>
</html>
```